Letterhead to Prospective Clients

Create a letterhead (word & canva) that I will use to send letters to prospective clients and also include the Coralwood Estate Partners Logo, My Contact Details and Interchangeable "Suburb". Use the same font and colour pallete

Maris Dulworth | "Suburb" Specialist - Tidewater & Surrounds
Mobile: 0417 862 095
Email: MD@CoralwoodEstatePartners.com.au

```html
<!DOCTYPE html>
<html lang="en">
<head>
<meta charset="UTF-8">
<title>Coralwood Estate Partners Letterhead</title>
<link href="https://fonts.googleapis.com/css2?family=Poppins:wght@300;400;500;600&display=swap" rel="stylesheet">
<style>
  :root {
    --navy: #01163b;
    --sand: #d6a77a;
    --mist: #d3dbe6;
    --paper: #ffffff;
    --backdrop: #eef0f4;
  }
  * { margin: 0; padding: 0; box-sizing: border-box; }
  html, body {
    width: 1200px;
    height: 1200px;
    overflow: hidden;
    background: var(--backdrop);
    font-family: "Poppins", sans-serif;
  }
  .letterhead {
    position: absolute;
    left: 136px;
    top: 0;
    width: 928px;
    height: 1200px;
    background: var(--paper);
    color: var(--navy);
  }
  .brand-header {
    position: absolute;
    top: 72px;
    left: 0;
    right: 0;
    text-align: center;
  }
  .brand-name {
    font-size: 26px;
    font-weight: 400;
    letter-spacing: 0.2em;
    line-height: 1;
    color: var(--navy);
    text-transform: uppercase;
  }
  .brand-watermark {
    position: absolute;
    top: 548px;
    left: 0;
    right: 0;
    text-align: center;
    font-size: 80px;
    font-weight: 300;
    line-height: 1;
    letter-spacing: 0.1em;
    color: var(--mist);
    text-transform: uppercase;
  }
  .agent-line {
    position: absolute;
    top: 1090px;
    left: 0;
    right: 0;
    text-align: center;
    font-size: 16px;
    font-weight: 400;
    color: var(--navy);
  }
  .agent-line strong { font-weight: 600; }
  .divider {
    position: absolute;
    top: 1129px;
    left: 0;
    width: 100%;
    height: 5px;
    display: flex;
  }
  .divider .navy-half { flex: 1; background: var(--navy); }
  .divider .sand-half { flex: 1; background: var(--sand); }
  .contact-row {
    position: absolute;
    top: 1145px;
    left: 0;
    right: 0;
    display: flex;
    justify-content: center;
    align-items: center;
    gap: 48px;
    font-size: 16px;
    font-weight: 400;
    color: var(--navy);
  }
  .contact-item {
    display: flex;
    align-items: center;
    gap: 16px;
  }
  .contact-item svg { display: block; }
</style>
</head>
<body>
  <main class="letterhead">
    <header class="brand-header">
      <div class="brand-name">Coralwood Estate Partners</div>
    </header>

    <div class="brand-watermark" aria-hidden="true">Coralwood</div>

    <footer>
      <p class="agent-line"><strong>Maris Dulworth |</strong> "Suburb" Specialist - Tidewater &amp; Surrounds</p>
      <div class="divider"><span class="navy-half"></span><span class="sand-half"></span></div>
      <div class="contact-row">
        <div class="contact-item">
          <svg width="18" height="18" viewBox="0 0 24 24" aria-hidden="true">
            <path fill="#d6a77a" d="M6.6 10.8c1.4 2.8 3.8 5.1 6.6 6.6l2.2-2.2c.3-.3.7-.4 1-.2 1.1.4 2.3.6 3.6.6.6 0 1 .4 1 1V20c0 .6-.4 1-1 1C10.6 21 3 13.4 3 4c0-.6.4-1 1-1h3.5c.6 0 1 .4 1 1 0 1.3.2 2.5.6 3.6.1.3 0 .7-.2 1z"/>
          </svg>
          <span>0417 862 095</span>
        </div>
        <div class="contact-item">
          <svg width="20" height="14" viewBox="0 0 20 14" aria-hidden="true">
            <rect x="0.5" y="0.5" width="19" height="13" fill="#d6a77a"/>
            <path d="M1 1l9 7 9-7M1 13l6.5-6M19 13l-6.5-6" stroke="#ffffff" stroke-width="1" fill="none"/>
          </svg>
          <span>MD@CoralwoodEstatePartners.com.au</span>
        </div>
      </div>
    </footer>
  </main>
</body>
</html>
```